I need a business Card Design for my practice , i am clinical herbalist. I am a herbalist specializing in Lyme disease, autism, autoimmune diseases, difficult to cure diseasesDifficult to cure diseases. In my innovative practice i link traditional medicine, herbs with science, immunologu ,pharmacology.

Industry/Entity Type

Business

Contact Information for Business Card

My company name : OŚRODEK ZIELNIK
My name : Piotr Kaleta
Name of my profession : Fitoterapeuta
In Polish language Fitoterapeuta is Herbalist .

e-mail: piotrkaleta@osrodekzielnik.com
www.osrodek-zielnik.pl
phone : 604 587 231
My company adress : Dąbrowa Sitnicka 41 , 38-415 Lużna
I dont have logo .

Requirements
Nice to have
• My company

```html
<!DOCTYPE html>
<html lang="pl">
<head>
<meta charset="utf-8">
<title>Ośrodek Zielnik – wizytówka</title>
<link rel="stylesheet" href="https://fonts.googleapis.com/css2?family=Cinzel:wght@400;600;700&display=swap">
<style>
  :root {
    --backdrop: #e9ebe6;
    --leaf-light: #7fae3c;
    --leaf-light-deep: #6a9a2e;
    --leaf-dark: #3f6a26;
    --leaf-darker: #2c4d1c;
    --paper: #f7f9f8;
    --ink-white: #ffffff;
    --ink-sage: #5b7a45;
    --ink-forest: #3f6a26;
    --ink-fresh: #7aa63a;
  }
  html, body {
    margin: 0;
    width: 1200px;
    height: 1010px;
    overflow: hidden;
    background: var(--backdrop);
  }
  .canvas {
    position: relative;
    width: 1200px;
    height: 1010px;
  }
  .card {
    position: absolute;
    left: 100px;
    top: 227px;
    width: 1000px;
    height: 556px;
    box-shadow: 0 14px 34px rgba(0,0,0,.18);
    font-family: "Cinzel", serif;
    overflow: hidden;
  }
  .card-shapes { position: absolute; inset: 0; }
  .person {
    position: absolute;
    left: 62px;
    top: 100px;
  }
  .person-name {
    margin: 0;
    font-size: 30px;
    font-weight: 700;
    color: var(--ink-white);
    letter-spacing: .5px;
  }
  .person-role {
    margin: 4px 0 0;
    font-size: 24px;
    font-weight: 600;
    color: var(--ink-sage);
  }
  .contact {
    position: absolute;
    left: 62px;
    top: 218px;
    margin: 0;
    padding: 0;
    list-style: none;
    font-size: 24px;
    line-height: 36px;
    color: var(--ink-white);
  }
  .company {
    position: absolute;
    right: 48px;
    top: 215px;
    text-align: right;
  }
  .company-name {
    margin: 0;
    font-size: 38px;
    font-weight: 700;
    color: var(--ink-forest);
    letter-spacing: 1px;
  }
  .company-site {
    margin: 4px 0 0;
    font-size: 24px;
    color: var(--ink-fresh);
  }
  .mark {
    position: absolute;
    left: 562px;
    top: 478px;
    display: flex;
    align-items: center;
    gap: 8px;
    font-size: 15px;
    font-weight: 600;
    color: var(--ink-white);
    white-space: nowrap;
  }
  .mark-dot {
    width: 12px;
    height: 12px;
    border-radius: 50%;
    background: var(--ink-white);
  }
</style>
</head>
<body>
<div class="canvas">
  <section class="card">
    <svg class="card-shapes" width="1000" height="556" viewBox="0 0 1000 556" aria-hidden="true">
      <defs>
        <linearGradient id="band-dark" x1="0" y1="0" x2="1" y2="1">
          <stop offset="0" stop-color="#3f6a26"/>
          <stop offset="1" stop-color="#2c4d1c"/>
        </linearGradient>
        <linearGradient id="band-light" x1="0" y1="0" x2="1" y2="1">
          <stop offset="0" stop-color="#7fae3c"/>
          <stop offset="1" stop-color="#6a9a2e"/>
        </linearGradient>
      </defs>
      <rect width="1000" height="556" fill="url(#band-dark)"/>
      <path d="M0,0 L40,0 Q420,180 565,556 L0,556 Z" fill="url(#band-light)"/>
      <path d="M120,0 L1000,0 L1000,556 L795,556 Q560,160 120,0 Z" fill="#f7f9f8"/>
    </svg>

    <div class="person">
      <h1 class="person-name">PIOTR KALETA</h1>
      <p class="person-role">FITOTERAPEUTA</p>
    </div>

    <ul class="contact">
      <li>PHONE: 604 587 231</li>
      <li>DĄBROWA SITNICKA 41 , 38-415 ZALESIE</li>
      <li>PIOTRKALETA@OSRODEKZIELNIK.COM</li>
    </ul>

    <div class="company">
      <h2 class="company-name">OŚRODEK ZIELNIK</h2>
      <p class="company-site">WWW.OSRODEK-ZIELNIK.PL</p>
    </div>

    <div class="mark">
      <span class="mark-dot"></span>
      <span>OŚRODEK ZIELNIK</span>
    </div>
  </section>
</div>
</body>
</html>
```